Quorvantelline.com

I need a site that I can sell dewatering equipment to the construction industry.
Ie, pipes fittings pumps and other such things needed to remove the groundwater on construction sites. Here in Florida, it’s needed almost everywhere seeing we are at sea level.
I want to be able to sell these products on the site and receive

Coded - Design and coding required

1 page

```html
<!DOCTYPE html>
<html lang="en">
<head>
<meta charset="utf-8">
<title>Quorvantelline — Dewatering Equipment</title>
<link rel="stylesheet" href="https://fonts.googleapis.com/css2?family=Exo+2:wght@600;700&family=Lato:wght@400;700&family=Raleway:wght@500;600;700&display=swap">
<style>
:root{
  --blue:#0a90dc;
  --navy:#0b379a;
  --deep:#0d3788;
  --ink:#2b2b2b;
  --muted:#777;
  --light:#f1f2f4;
  --white:#fff;
}
*{margin:0;padding:0;box-sizing:border-box}
html,body{width:1200px;height:3830px;overflow:hidden}
body{position:relative;font-family:"Lato",sans-serif;color:var(--ink);background:var(--white)}
.abs{position:absolute}
.img{position:absolute}
.display{font-family:"Exo 2",sans-serif;font-weight:700}

.header{left:0;top:0;width:1200px;height:135px;background:var(--white)}
.brand{left:78px;top:30px;display:flex;align-items:center;gap:14px}
.brand-mark{width:56px;height:56px;border-radius:50%;background:var(--blue)}
.brand-name{font-family:"Raleway",sans-serif;font-weight:700;font-size:30px;color:#555;letter-spacing:1px}
.call{left:855px;top:42px;display:flex;align-items:center;gap:14px}
.call small{display:block;font-size:15px;color:#555}
.call strong{display:block;font-size:24px;color:var(--navy);font-weight:700}
.badge{left:1068px;top:46px;width:56px;height:56px;border-radius:8px;background:#f2a81d}

.nav{left:0;top:135px;width:1200px;height:64px;background:var(--navy)}
.nav ul{position:absolute;left:80px;top:0;display:flex;list-style:none;height:64px;align-items:center}
.nav li{color:var(--white);font-size:16px;font-family:"Raleway",sans-serif;font-weight:600;margin-right:48px}
.search{left:893px;top:149px;width:230px;height:36px;border:1.5px solid var(--white);border-radius:18px;color:var(--white);font-size:14px;padding:9px 16px}

.hero{left:0;top:199px;width:1200px;height:575px;background:linear-gradient(180deg,#5f7f93 0%,#45657a 45%,#3a4d55 100%)}
.hero-shade{left:0;top:199px;width:1200px;height:575px;background:rgba(10,25,40,.35)}
.hero h1{left:0;width:1200px;top:345px;text-align:center;color:var(--white);font-size:50px;letter-spacing:2px}
.hero p{left:330px;width:540px;top:425px;text-align:center;color:var(--white);font-size:17px;line-height:30px}
.btn{position:absolute;height:64px;border-radius:32px;display:flex;align-items:center;justify-content:center;font-size:18px;font-weight:700;text-transform:uppercase}
.btn-blue{background:var(--blue);color:var(--white)}
.btn-white{background:var(--white);color:var(--navy)}
.dots{left:572px;top:692px;display:flex;gap:8px}
.dots i{width:14px;height:14px;border-radius:50%;background:var(--white);display:block}
.dots i.on{background:var(--blue)}

.thumb{position:absolute;top:791px;width:180px;height:158px;border:1px solid #ddd;background:var(--white)}
.thumb .img{left:12px;top:12px;width:154px;height:132px}
.arrow{position:absolute;width:40px;height:40px;border-radius:50%;background:var(--blue);color:var(--white);display:flex;align-items:center;justify-content:center}

.about h2{left:77px;top:1005px;font-family:"Raleway",sans-serif;font-size:38px;font-weight:700;color:var(--blue)}
.about h2 b{color:var(--navy)}
.about p{left:77px;top:1068px;width:545px;font-size:13.5px;line-height:25px;color:#555}
.video{left:684px;top:1013px;width:439px;height:269px;background:linear-gradient(135deg,#2f7fae,#1b5b87 60%,#2a6f97)}
.play{left:870px;top:1112px;width:70px;height:70px}

.services{left:0;top:1345px;width:1200px;height:672px;background:linear-gradient(180deg,#27343c,#1b2429 60%,#2c3a41)}
.sec-title{position:absolute;left:0;width:1200px;text-align:center;font-size:38px}
.sec-title .rule{display:inline-block;width:95px;height:1px;vertical-align:middle;margin:0 22px}
.service{position:absolute;width:289px;height:205px;background:var(--light);text-align:center}
.service svg{margin-top:22px}
.service h3{font-family:"Raleway",sans-serif;font-size:16px;font-weight:700;color:var(--blue);margin-top:10px}
.service p{font-size:13px;color:var(--muted);line-height:23px;margin:10px auto 0;width:200px}

.pump{position:absolute;width:255px;height:365px;border:1px solid #e3e3e3;background:var(--white);text-align:center}
.pump.active{background:#eeeff1;border-color:#ddd}
.pump .img{left:50%;transform:translateX(-50%);width:170px;height:165px}
.pump h3{position:absolute;left:0;width:100%;font-family:"Raleway",sans-serif;font-size:20px;font-weight:700;color:var(--navy)}
.pump p{position:absolute;left:0;width:100%;font-size:13px;color:var(--muted)}
.pump .buy{position:absolute;left:50%;transform:translateX(-50%);width:104px;height:40px;border-radius:20px;background:var(--blue);color:var(--white);font-size:14px;font-weight:700;display:flex;align-items:center;justify-content:center}
.pump.active .buy{background:var(--deep)}

.projects{left:0;top:2732px;width:1200px;height:638px;background:linear-gradient(180deg,#4a3a2e,#2e2620 55%,#4b3b2e)}
.shot{position:absolute}

.contact{left:0;top:3370px;width:1200px;height:396px;background:var(--light)}
.field{position:absolute;background:var(--white);font-size:14px;color:#666;padding:13px 12px}
.info{position:absolute;left:735px;font-size:14px;color:#555;line-height:24px}
.info-ico{position:absolute;left:692px;width:24px;height:24px}
.links{left:965px;top:3518px;list-style:none}
.links li{font-size:14px;color:#555;line-height:25.5px;position:relative;padding-left:16px}
.links li::before{content:"";position:absolute;left:0;top:10px;width:6px;height:6px;border-radius:50%;background:var(--navy)}
.footer{left:0;top:3766px;width:1200px;height:64px;background:var(--navy);color:var(--white);font-size:14px;text-align:center;line-height:64px}
</style>
</head>
<body>

<header class="abs header">
  <div class="abs brand"><span class="brand-mark"></span><span class="brand-name">QUORVANTELLINE</span></div>
  <div class="abs call">
    <svg width="38" height="38" viewBox="0 0 24 24"><path fill="#0a90dc" d="M6.6 10.8a15 15 0 0 0 6.6 6.6l2.2-2.2c.3-.3.7-.4 1-.2 1.1.4 2.3.6 3.6.6.6 0 1 .4 1 1V20c0 .6-.4 1-1 1A17 17 0 0 1 3 4c0-.6.4-1 1-1h3.5c.6 0 1 .4 1 1 0 1.3.2 2.5.6 3.6.1.3 0 .7-.2 1z"/></svg>
    <div><small>Call Us Now</small><strong>123-456-7890</strong></div>
  </div>
  <div class="abs badge"></div>
</header>

<nav class="abs nav">
  <ul><li>Home</li><li>About</li><li>Pumps</li><li>Services</li><li>Projects</li><li>Contact Us</li></ul>
</nav>
<div class="abs search">Search...
  <svg class="abs" style="right:14px;top:8px" width="18" height="18" viewBox="0 0 24 24"><circle cx="10" cy="10" r="7" fill="none" stroke="#fff" stroke-width="2.4"/><path d="M15 15l6 6" stroke="#fff" stroke-width="2.4"/></svg>
</div>

<section>
  <div class="abs hero" role="img" aria-label="Industrial water treatment site with blue tanks and pipework"></div>
  <div class="abs hero-shade"></div>
  <div class="hero">
    <h1 class="abs display">QUORVANTELLINE</h1>
    <p class="abs">Lorem Ipsum is simply dummy text of the printing and typesetting industry. Lorem Ipsum has been the industry's standard dummy text ever since the 1500s.</p>
  </div>
  <div class="btn btn-blue" style="left:427px;top:550px;width:177px">Contact Us</div>
  <div class="btn btn-white" style="left:606px;top:550px;width:166px">Buy Now</div>
  <div class="abs dots"><i></i><i class="on"></i><i></i></div>
</section>

<section>
  <div class="arrow" style="left:57px;top:852px"><svg width="14" height="14" viewBox="0 0 10 10"><path d="M7 1L3 5l4 4" fill="none" stroke="#fff" stroke-width="2"/></svg></div>
  <div class="thumb" style="left:115px"><div class="img" role="img" aria-label="Blue inline pumps" style="background:linear-gradient(135deg,#e9f2f6,#5fa7c4 60%,#e9f2f6)"></div></div>
  <div class="thumb" style="left:311px"><div class="img" role="img" aria-label="Green portable engine pump" style="background:linear-gradient(135deg,#eef2ea,#3f8a3a 55%,#eef2ea)"></div></div>
  <div class="thumb" style="left:511px"><div class="img" role="img" aria-label="Blue gear pump" style="background:linear-gradient(135deg,#edf0f5,#1e4f9c 55%,#edf0f5)"></div></div>
  <div class="thumb" style="left:707px"><div class="img" role="img" aria-label="Diaphragm pump" style="background:linear-gradient(135deg,#f3f3f3,#9a9a9a 55%,#f3f3f3)"></div></div>
  <div class="thumb" style="left:906px"><div class="img" role="img" aria-label="Red fire pump set" style="background:linear-gradient(135deg,#f6eeee,#c92a2a 55%,#f6eeee)"></div></div>
  <div class="arrow" style="left:1100px;top:852px"><svg width="14" height="14" viewBox="0 0 10 10"><path d="M3 1l4 4-4 4" fill="none" stroke="#fff" stroke-width="2"/></svg></div>
</section>

<section class="about">
  <h2 class="abs">About <b>QUORVANTELLINE</b></h2>
  <p class="abs">Lorem Ipsum is simply dummy text of the printing and typesetting industry. Lorem Ipsum has been the industry's standard dummy text ever since the 1500s, when an unknown printer took a galley of type and scrambled it to make a type specimen book. It has survived not only five centuries, but also the leap into electronic typesetting, remaining essentially unchanged. It was popularised in the 1960s.</p>
  <div class="btn btn-blue" style="left:77px;top:1221px;width:167px;height:62px;font-size:16px">Read More</div>
  <div class="abs video" role="img" aria-label="Worker handling pipe fittings on site"></div>
  <svg class="abs play" viewBox="0 0 70 70"><circle cx="35" cy="35" r="32" fill="none" stroke="#fff" stroke-width="3"/><circle cx="35" cy="35" r="22" fill="#fff" opacity=".85"/><path d="M30 25l14 10-14 10z" fill="#1b5b87"/></svg>
</section>

<section>
  <div class="abs services" role="img" aria-label="Water splashing over a dark surface"></div>
  <h2 class="sec-title display" style="top:1400px;color:#fff"><span class="rule" style="background:#fff"></span>Our SERVICES<span class="rule" style="background:#fff"></span></h2>

  <div class="service" style="left:133px;top:1494px">
    <svg width="56" height="56" viewBox="0 0 56 56"><rect x="22" y="6" width="12" height="6" fill="#0b379a"/><circle cx="28" cy="28" r="14" fill="#0a90dc"/><rect x="4" y="24" width="12" height="8" fill="#0b379a"/><rect x="40" y="24" width="12" height="8" fill="#0b379a"/><rect x="14" y="44" width="28" height="6" fill="#0b379a"/></svg>
    <h3>Pumping Services</h3><p>Lorem Ipsum is simply dummy typesetting industry.</p>
  </div>
  <div class="service" style="left:454px;top:1494px">
    <svg width="56" height="56" viewBox="0 0 56 56"><path d="M14 10c6 10 10 16 10 22a10 10 0 0 1-20 0c0-6 4-12 10-22z" fill="#0a90dc"/><path d="M38 10c6 10 10 16 10 22a10 10 0 0 1-20 0c0-6 4-12 10-22z" fill="#0b379a"/><rect x="6" y="46" width="44" height="5" fill="#0b379a"/></svg>
    <h3>Dewatering</h3><p>Lorem Ipsum is simply dummy typesetting industry.</p>
  </div>
  <div class="service" style="left:776px;top:1494px">
    <svg width="56" height="56" viewBox="0 0 56 56"><rect x="6" y="18" width="30" height="18" fill="#0b379a"/><rect x="12" y="10" width="16" height="8" fill="#0a90dc"/><circle cx="44" cy="30" r="8" fill="none" stroke="#0a90dc" stroke-width="4"/><rect x="4" y="40" width="36" height="8" rx="4" fill="#0a90dc"/></svg>
    <h3>One-Pass Trenching</h3><p>Lorem Ipsum is simply dummy typesetting industry.</p>
  </div>
  <div class="service" style="left:133px;top:1733px">
    <svg width="56" height="56" viewBox="0 0 56 56"><path d="M4 48V28l10-6v6l10-6v6l10-6v26z" fill="#0b379a"/><path d="M44 6l-8 42h16z" fill="none" stroke="#0a90dc" stroke-width="3"/><path d="M38 18h12M37 28h14" stroke="#0a90dc" stroke-width="3"/></svg>
    <h3>Power Generation</h3><p>Lorem Ipsum is simply dummy typesetting industry.</p>
  </div>
  <div class="service" style="left:454px;top:1733px">
    <svg width="56" height="56" viewBox="0 0 56 56"><rect x="12" y="12" width="28" height="36" rx="4" fill="none" stroke="#0b379a" stroke-width="4"/><path d="M26 22c4 6 6 9 6 12a6 6 0 0 1-12 0c0-3 2-6 6-12z" fill="#0a90dc"/><rect x="40" y="20" width="10" height="5" fill="#0b379a"/></svg>
    <h3>Water Filtration &amp; Treatment</h3><p>Lorem Ipsum is simply dummy typesetting industry.</p>
  </div>
  <div class="service" style="left:776px;top:1733px">
    <svg width="56" height="56" viewBox="0 0 56 56"><path d="M28 4l-12 44h24z" fill="none" stroke="#0b379a" stroke-width="4"/><path d="M20 30h16M23 18h10" stroke="#0a90dc" stroke-width="4"/><rect x="10" y="46" width="36" height="6" fill="#0b379a"/></svg>
    <h3>Drilling</h3><p>Lorem Ipsum is simply dummy typesetting industry.</p>
  </div>
</section>

<section>
  <h2 class="sec-title display" style="top:2068px;color:var(--blue)"><span class="rule" style="background:#ccc"></span>Our Different <span style="color:var(--navy)">PUMPS</span><span class="rule" style="background:#ccc"></span></h2>

  <div class="pump" style="left:77px;top:2196px">
    <div class="img" role="img" aria-label="Lobe pump" style="top:30px;background:linear-gradient(135deg,#fff,#8d97a2 50%,#2a5fb0 75%,#fff)"></div>
    <h3 style="top:225px">Lobe Pumps</h3><p style="top:260px">Lorem Ipsum Dummy</p><div class="buy" style="top:295px">BUY NOW</div>
  </div>
  <div class="pump active" style="left:340px;top:2160px;width:257px;height:432px">
    <div class="img" role="img" aria-label="Jet pump" style="top:30px;height:200px;background:linear-gradient(135deg,#eeeff1,#1f2f7a 50%,#c9a54a 75%,#eeeff1)"></div>
    <h3 style="top:260px">Jet Pumps</h3><p style="top:295px">Lorem Ipsum Dummy</p><div class="buy" style="top:332px">BUY NOW</div>
  </div>
  <div class="pump" style="left:603px;top:2196px;width:250px">
    <div class="img" role="img" aria-label="Slurry pump" style="top:30px;background:linear-gradient(135deg,#fff,#e6c21a 50%,#333 75%,#fff)"></div>
    <h3 style="top:225px">Slurry Pump</h3><p style="top:260px">Lorem Ipsum Dummy</p><div class="buy" style="top:295px">BUY NOW</div>
  </div>
  <div class="pump" style="left:865px;top:2196px;width:253px">
    <div class="img" role="img" aria-label="Trash pump" style="top:30px;background:linear-gradient(135deg,#fff,#d94f1c 50%,#222 75%,#fff)"></div>
    <h3 style="top:225px">Trash Pumps</h3><p style="top:260px">Lorem Ipsum Dummy</p><div class="buy" style="top:295px">BUY NOW</div>
  </div>

  <div class="arrow" style="left:554px;top:2627px;background:var(--deep)"><svg width="14" height="14" viewBox="0 0 10 10"><path d="M7 1L3 5l4 4" fill="none" stroke="#fff" stroke-width="2"/></svg></div>
  <div class="arrow" style="left:604px;top:2627px;background:#fff;box-shadow:0 2px 5px rgba(0,0,0,.3)"><svg width="14" height="14" viewBox="0 0 10 10"><path d="M3 1l4 4-4 4" fill="none" stroke="#333" stroke-width="2"/></svg></div>
</section>

<section>
  <div class="abs projects" role="img" aria-label="Open-pit construction site"></div>
  <h2 class="sec-title display" style="top:2788px;color:#fff"><span class="rule" style="background:#fff"></span>Our Work Projects<span class="rule" style="background:#fff"></span></h2>
  <div class="shot" role="img" aria-label="Pump station on site" style="left:77px;top:2875px;width:250px;height:207px;background:linear-gradient(160deg,#8fb7d6,#3c7ea6 50%,#b57a3a)"></div>
  <div class="shot" role="img" aria-label="Industrial plant with smoking chimneys" style="left:342px;top:2875px;width:513px;height:207px;background:linear-gradient(180deg,#c7793a,#8c4a25 55%,#2a1d15)"></div>
  <div class="shot" role="img" aria-label="Blue pressure tanks" style="left:871px;top:2875px;width:252px;height:207px;background:linear-gradient(160deg,#cfd9e2,#3467a8 55%,#6d7378)"></div>
  <div class="shot" role="img" aria-label="Pumps in plant room" style="left:77px;top:3097px;width:250px;height:209px;background:linear-gradient(160deg,#8c8c86,#a8742f 55%,#5c5248)"></div>
  <div class="shot" role="img" aria-label="Green industrial pumps" style="left:342px;top:3097px;width:253px;height:209px;background:linear-gradient(160deg,#4b5d60,#2e6e6a 55%,#20302f)"></div>
  <div class="shot" role="img" aria-label="Pipe manifold with red valves" style="left:605px;top:3097px;width:253px;height:209px;background:linear-gradient(160deg,#8d9398,#b5b9bc 45%,#9c2e2e)"></div>
  <div class="shot" role="img" aria-label="Yellow pump by the water" style="left:871px;top:3097px;width:252px;height:209px;background:linear-gradient(180deg,#9fc3dd,#7aa1bd 55%,#c9a23a)"></div>
</section>

<section>
  <div class="abs contact"></div>
  <h2 class="sec-title display" style="top:3428px;color:var(--blue)"><span class="rule" style="background:#ccc"></span>Contact <span style="color:var(--navy)">US</span><span class="rule" style="background:#ccc"></span></h2>

  <div class="field" style="left:77px;top:3528px;width:260px;height:46px">First Name :</div>
  <div class="field" style="left:77px;top:3592px;width:260px;height:46px">Email :</div>
  <div class="field" style="left:77px;top:3656px;width:260px;height:46px">Phone :</div>
  <div class="field" style="left:350px;top:3528px;width:258px;height:110px">Message / Comments :</div>
  <div class="btn btn-blue" style="left:350px;top:3654px;width:258px;height:50px;border-radius:25px;font-size:16px">Submit Now</div>

  <svg class="info-ico" style="top:3526px" viewBox="0 0 24 24"><path fill="#0b379a" d="M6.6 10.8a15 15 0 0 0 6.6 6.6l2.2-2.2c.3-.3.7-.4 1-.2 1.1.4 2.3.6 3.6.6.6 0 1 .4 1 1V20c0 .6-.4 1-1 1A17 17 0 0 1 3 4c0-.6.4-1 1-1h3.5c.6 0 1 .4 1 1 0 1.3.2 2.5.6 3.6.1.3 0 .7-.2 1z"/></svg>
  <div class="info" style="top:3526px">123 456 7890</div>
  <svg class="info-ico" style="top:3564px" viewBox="0 0 24 24"><rect x="2" y="5" width="20" height="14" fill="#0b379a"/><path d="M2 5l10 8 10-8" fill="none" stroke="#fff" stroke-width="1.6"/></svg>
  <div class="info" style="top:3564px">info@quorvantelline.com</div>
  <svg class="info-ico" style="top:3604px" viewBox="0 0 24 24"><path fill="#0b379a" d="M12 2a7 7 0 0 0-7 7c0 5 7 13 7 13s7-8 7-13a7 7 0 0 0-7-7z"/><circle cx="12" cy="9" r="2.6" fill="#fff"/></svg>
  <div class="info" style="top:3602px;width:200px">Lorem Ipsum simply dummy typesetting industry.</div>

  <ul class="abs links"><li>Home</li><li>About</li><li>Pumps</li><li>Services</li><li>Projects</li><li>Contact</li></ul>
</section>

<footer class="abs footer">© Copyright 2018 <b>QUORVANTELLINE</b> &nbsp;| All Rights Reserved.</footer>

</body>
</html>
```